Riverbend Haven Home Care-Nursing Assessment Form

I am creating a Nursing Assessment Form (which is used to be an intake form for all new patients) for my new home care company, Riverbend Haven Home Care.

It is 15 pages and pretty comprehensive as this is a very regulated field. I have all the necessary content and information attached in the word document below. Now, I am seeking a designer to make it look professional, cohesive and easy to read/ follow.
In order for your Word Document Design to be selected, you must:

1. As mentioned previously, make it easy to read/follow. There should be enough spacing, room to write out all necessary notes, fill out check marks...etc...
2. It should look professional.
3. It should be attractive and eye pleasing. Attached you will find our logo-kindly incorporate it's style into the project as well. The logo should be placed on top of each page.
4. Lastly, we need a Word Document version AND PDF Fillable Option. The fillable PDF should Auto Fill for the Name and Start of Care (SOC) Date.

I have attached a sample form below as well. This is how I envision the finished project to look. Of course, I am open to other suggestions as look as it meets the aforementioned requirements.

Thank you! May the best man or woman win!
Our team looks forward to working with our designer on this project!

Industry/Entity Type

Home Health Care

Font styles to use
Sans Serif

Colors
0255a3
9bcb3c

Requirements
Must have
• Refer to Project Description above.
Nice to have
We must be given a Word Document Option and PDF Fillable Option.

```html
<!DOCTYPE html>
<html lang="en">
<head>
<meta charset="utf-8">
<title>Riverbend Haven Home Care – Initial Assessment Form</title>
<link href="https://fonts.googleapis.com/css2?family=Montserrat:wght@700;800&family=Roboto+Condensed:wght@400;700&display=swap" rel="stylesheet">
<style>
  :root{
    --brand-blue:#0255a3;
    --brand-navy:#0a3a8c;
    --brand-green:#9bcb3c;
    --panel-tint:#e8eefb;
    --ink:#111;
    --backdrop:#e6eaf0;
  }
  *{box-sizing:border-box;margin:0;padding:0}
  html,body{width:1200px;height:750px;overflow:hidden;background:var(--backdrop)}
  body{font-family:"Roboto Condensed",Arial,sans-serif;color:var(--ink)}
  .page{position:absolute;left:322px;top:15px;width:556px;height:720px;background:#fff;box-shadow:0 1px 4px rgba(0,0,0,.25)}
  .brand{position:absolute;left:28px;top:30px;width:100px;display:flex;align-items:center;gap:5px}
  .brand-dot{width:14px;height:14px;border-radius:50%;background:var(--brand-blue);flex:none}
  .brand-name{font-family:"Montserrat",sans-serif;font-weight:800;font-size:9px;line-height:1.1;color:var(--brand-blue)}
  .tag{position:absolute;left:169px;top:22px;width:184px;height:13px;background:var(--brand-green);color:#fff;font-family:"Montserrat",sans-serif;font-weight:700;font-size:8.6px;line-height:13px;text-align:center;letter-spacing:.2px}
  .title{position:absolute;left:168px;top:34px;font-family:"Montserrat",sans-serif;font-weight:800;font-size:25px;color:var(--brand-navy);letter-spacing:-.2px}
  .rule{position:absolute;left:28px;top:81px;width:499px;height:4px;background:linear-gradient(90deg,var(--brand-green) 0 95px,var(--brand-navy) 95px)}
  .panel{position:absolute;left:28px;top:86px;width:499px;height:63px;background:var(--panel-tint)}
  .row{position:absolute;left:28px;right:29px;height:9px;display:flex;align-items:flex-end;font-size:7px;line-height:8px;white-space:nowrap}
  .row.in-panel{left:36px;right:37px}
  .b{font-weight:700}
  .h{font-weight:700;text-decoration:underline}
  .fill{display:inline-block;height:7px;border-bottom:.7px solid var(--ink);flex:none}
  .fill.grow{flex:1}
  .cb{display:inline-block;width:6.5px;height:6.5px;border:.8px solid var(--ink);margin-right:3px;flex:none;position:relative;top:-.5px}
  .opt{display:inline-flex;align-items:center;margin-right:0}
  .grid{position:absolute;left:28px;top:368px;width:499px;display:grid;grid-template-columns:166px 178px 1fr;grid-auto-rows:12px;font-size:7px}
  .grid .opt{align-items:center}
  .ability .lbl{width:166px;flex:none}
  .line{position:absolute;left:28px;width:499px;border-bottom:.7px solid var(--ink)}
</style>
</head>
<body>
<main class="page">
  <div class="brand"><span class="brand-dot"></span><span class="brand-name">RIVERBEND HAVEN HOME CARE</span></div>
  <div class="tag">RIVERBEND HAVEN HOME CARE</div>
  <h1 class="title">Initial Assessment Form</h1>
  <div class="row" style="left:170px;top:63px"><span class="b">Name :&nbsp;</span><span class="fill" style="width:222px"></span><span class="b">&nbsp;&nbsp;SOC Date :&nbsp;</span><span class="fill grow"></span></div>
  <div class="rule"></div>

  <section class="panel"></section>
  <div class="row in-panel b" style="top:95px">Patient’s Name<span class="fill grow"></span>Gender<span class="fill" style="width:37px"></span>MR#<span class="fill" style="width:39px"></span>Date<span class="fill" style="width:37px"></span></div>
  <div class="row in-panel b" style="top:107px">Primary Diagnosis<span class="fill" style="width:197px"></span>Secondary Diagnosis&nbsp;<span class="fill grow"></span></div>
  <div class="row in-panel b" style="top:119px">Other Pertinent Diagnosis<span class="fill" style="width:228px"></span>PCP name<span class="fill grow"></span></div>
  <div class="row in-panel b" style="top:131px">Other Physician Name&nbsp;<span class="fill" style="width:236px"></span></div>

  <div class="row" style="top:151px"><span class="b" style="width:47px">Prognosis:</span><span class="opt" style="width:47px"><span class="cb"></span>Poor</span><span class="opt" style="width:43px"><span class="cb"></span>Fair</span><span class="opt" style="width:48px"><span class="cb"></span>Good</span><span class="opt"><span class="cb"></span>Excellent</span></div>
  <div class="row" style="top:163px"><span class="b">Vital Signs:&nbsp;&nbsp;</span>Height:<span class="fill" style="width:30px"></span>Weight:<span class="fill" style="width:43px"></span>&nbsp;&nbsp;&nbsp;Temp:<span class="fill" style="width:42px"></span>&nbsp;&nbsp;&nbsp;Pulse:<span class="fill" style="width:45px"></span>&nbsp;&nbsp;&nbsp;Resp:<span class="fill" style="width:41px"></span>&nbsp;&nbsp;&nbsp;B/P:<span class="fill" style="width:45px"></span></div>
  <div class="row" style="top:175px"><span class="b">Allergies:&nbsp;</span><span class="fill" style="width:197px"></span></div>
  <div class="row" style="top:187px;right:34px"><span class="b">Past Medical and Surgical History:</span><span class="fill grow"></span></div>

  <div class="row h" style="top:207px">Support System :</div>
  <div class="row" style="top:219px">Married/Not Married/Single/Divorced/Widowed</div>
  <div class="row" style="top:231px">Lives Alone:&nbsp;<span class="opt" style="width:28px"><span class="cb"></span>Yes</span><span class="opt"><span class="cb"></span>No</span></div>
  <div class="row" style="top:244px">Family Composition:<span class="fill" style="width:264px"></span></div>
  <div class="row" style="top:255px">Legal Next of Kin:<span class="fill" style="width:166px"></span>Telephone:<span class="fill" style="width:118px"></span>/&nbsp;&nbsp;<span class="fill grow"></span></div>
  <div class="row" style="top:267px">Address:&nbsp;<span class="fill" style="width:190px"></span>E-mail:<span class="fill" style="width:130px"></span></div>
  <div class="row" style="top:279px"><span style="width:249px">Is significant other able, available, capable and willing to care for patient?</span><span class="opt" style="width:45px"><span class="cb"></span>Yes</span><span class="opt"><span class="cb"></span>No</span></div>
  <div class="row" style="top:291px">If No, explain:&nbsp;<span class="fill grow"></span></div>
  <div class="row" style="top:303px">Educational Needs of Patient/Family:&nbsp;<span class="fill grow"></span></div>

  <div class="row h" style="top:323px">Environment :</div>
  <div class="row" style="top:335px"><span class="opt" style="width:89px"><span class="cb"></span>Private Home</span><span class="opt" style="width:77px"><span class="cb"></span>Elevator</span><span class="opt" style="width:83px"><span class="cb"></span>Apartment</span><span class="opt"><span class="cb"></span>Walkup</span></div>

  <div class="row h" style="top:355px">Safety Hazards in the Home:&nbsp;</div>
  <div class="grid">
    <span class="opt"><span class="cb"></span>Sound structure</span><span class="opt"><span class="cb"></span>Safe Placement of Cords, Rugs and Furniture</span><span class="opt"><span class="cb"></span>Adequate Heating and Ventilation</span>
    <span class="opt"><span class="cb"></span>Adequate Cooking facility</span><span class="opt"><span class="cb"></span>Adequate Plumbing/Sanitation/ Running Water</span><span class="opt"><span class="cb"></span>Adequate Sleeping Arrangement</span>
    <span class="opt"><span class="cb"></span>Safe Gas/Electric Appliances</span><span class="opt"><span class="cb"></span>Grounded Plug for Equipment</span><span class="opt"><span class="cb"></span>Enough Electrical Outlets for Equipment</span>
    <span class="opt"><span class="cb"></span>Working Telephone in the Home</span><span class="opt"><span class="cb"></span>Safe storage for Supplies/Equipment/Meds?</span><span class="opt"><span class="cb"></span>Exits Free of Obstruction</span>
    <span class="opt"><span class="cb"></span>Working smoke detectors?</span><span class="opt"><span class="cb"></span>Fire extinguisher in home?</span><span class="opt"><span class="cb"></span>Infestations of pests?</span>
    <span class="opt"><span class="cb"></span>Neighborhood safe?</span>
  </div>
  <div class="row" style="top:439px">Comments:<span class="fill grow"></span></div>

  <div class="row h" style="top:458px">Caregiver’s Contact Information:</div>
  <div class="row" style="top:471px">Name:<span class="fill" style="width:284px"></span></div>
  <div class="row" style="top:482px">Telephone<span class="fill" style="width:103px"></span>/<span class="fill" style="width:169px"></span></div>
  <div class="row" style="top:495px">Address:&nbsp;<span class="fill" style="width:143px"></span>E-mail:&nbsp;<span class="fill" style="width:109px"></span></div>
  <div class="row" style="top:507px">Days / Time Available:&nbsp;<span class="fill" style="width:236px"></span></div>

  <div class="row h" style="top:527px">Caregivers Ability to Assist Patient / Able to Provide:</div>
  <div class="row ability" style="top:539px"><span class="lbl">Personal Care:</span><span class="opt" style="width:30px"><span class="cb"></span>Yes</span><span class="opt"><span class="cb"></span>No</span></div>
  <div class="row ability" style="top:551px"><span class="lbl">Mobility:</span><span class="opt" style="width:30px"><span class="cb"></span>Yes</span><span class="opt"><span class="cb"></span>No</span></div>
  <div class="row ability" style="top:563px"><span class="lbl">Prepare/Serve Meals:</span><span class="opt" style="width:30px"><span class="cb"></span>Yes</span><span class="opt"><span class="cb"></span>No</span></div>
  <div class="row ability" style="top:575px"><span class="lbl">Maintain Safe/Clean Environment:</span><span class="opt" style="width:30px"><span class="cb"></span>Yes</span><span class="opt"><span class="cb"></span>No</span></div>
  <div class="row ability" style="top:587px"><span class="lbl">Perform/ Assist with Procedures:</span><span class="opt" style="width:30px"><span class="cb"></span>Yes</span><span class="opt"><span class="cb"></span>No</span></div>
  <div class="row ability" style="top:599px"><span class="lbl">Caregiver has capacity to learn therapeutic regimen:</span><span class="opt" style="width:30px"><span class="cb"></span>Yes</span><span class="opt"><span class="cb"></span>No</span></div>
  <div class="row" style="top:611px">Comments:&nbsp;<span class="fill" style="width:180px"></span></div>

  <div class="row h" style="top:631px">Are There Any Signs of Abuse or Neglect from Family or Caregiver?:&nbsp;&nbsp;&nbsp;<span class="opt" style="width:32px"><span class="cb"></span>Yes</span><span class="opt"><span class="cb"></span>No&nbsp;</span></div>
  <div class="row h" style="top:642px">If Yes, describe:</div>
  <div class="line" style="top:661px"></div>
  <div class="line" style="top:670px"></div>
  <div class="line" style="top:679px"></div>
</main>
</body>
</html>
```